SKYVANTEX (drone photo and video) and Photogrammetry Services (mapping and 3D modeling)

We need a business card design for a SKYVANTEX. Our businesses provides (drone) Aerial Photo and Video Captures. However we also provide Photogrammetry (which is 3D modeling and mapping). We greatly value unique points of view taken of landscapes and subjects with aerial photography and videography. 3D modeling and mapping is the other area of focus and have an incredibly broad scope of applications and imaginative creativity.

Target Market(s)

Based out of Northern Virginia and serving the greater Virginia and Maryland areas

Industry/Entity Type

Drone Photo and video and Photogrammetry Services (mapping and 3D modeling)

Contact Information for Business Card

3D Models, Maps and Photo/Video Production name: Marcus Pettibone email: mqp@skyvantex.us website: skyvantex.us phone: 571-806-3394; please also include "Aerial Photo/Video and 3D Mapping/Modeling"

Requirements
Must have
• Please make this design vertical and double sided. The selection box is not letting me choose Double Sided but that is my wish. Incorporate uploaded LOGO and color scheme
Nice to have
• Preferably does not feel too crowded and balances not having an exaggerated amount of distracting detail
Should not have
• do not cram bullet points or text in long form

```html
<!DOCTYPE html>
<html lang="en">
<head>
<meta charset="utf-8">
<title>SKYVANTEX Business Card</title>
<link href="https://fonts.googleapis.com/css2?family=Roboto:wght@400;500;700&display=swap" rel="stylesheet">
<style>
  :root {
    --stage: #cbcbcb;
    --card-white: #ffffff;
    --card-navy: #212b35;
    --brand-red: #e3211f;
    --brand-orange: #f39a12;
    --ink: #141414;
    --muted: #55595e;
    --slate: #6f8796;
    --slate-light: #93a9b6;
    --photo-light: #f1f2f3;
    --photo-mid: #c9ccd0;
  }
  * { margin: 0; padding: 0; box-sizing: border-box; }
  html, body {
    width: 1200px; height: 848px; overflow: hidden;
    background: var(--stage);
    font-family: "Roboto", Arial, sans-serif;
  }
  .canvas { position: relative; width: 1200px; height: 848px; }

  .card { position: absolute; box-shadow: 0 10px 24px rgba(0,0,0,0.18); overflow: hidden; }

  /* Front side */
  .card-front {
    left: 170px; top: 164px; width: 350px; height: 500px;
    background: var(--card-white);
    display: flex; flex-direction: column;
    padding-top: 52px;
  }
  .brand {
    display: flex; align-items: center; justify-content: center; gap: 12px;
  }
  .brand-dot {
    width: 30px; height: 30px; border-radius: 50%;
    background: var(--brand-orange);
  }
  .brand-name {
    font-weight: 700; font-size: 34px; letter-spacing: 1px;
    color: var(--brand-red);
  }
  .holder {
    margin: 22px 0 0 52px;
  }
  .holder-name {
    font-weight: 500; font-size: 18px; color: var(--ink); line-height: 1.2;
  }
  .holder-services {
    font-size: 12.5px; color: var(--muted); line-height: 1.3; margin-top: 4px;
  }
  .contact-list {
    list-style: none; margin: 18px 0 0 52px;
  }
  .contact-item {
    display: flex; align-items: center; gap: 12px;
    font-size: 17px; color: var(--ink); line-height: 1; margin-bottom: 12px;
  }
  .contact-icon { width: 17px; height: 17px; flex: none; }
  .drone-photo {
    margin-top: auto; width: 100%; height: 180px;
    background: linear-gradient(180deg, var(--card-white) 0%, var(--photo-light) 45%, var(--photo-mid) 100%);
  }

  /* Back side */
  .card-back {
    left: 580px; top: 264px; width: 470px; height: 330px;
    background: var(--card-navy);
    display: flex; align-items: center; justify-content: center;
  }
  .back-brand { display: flex; align-items: center; gap: 18px; }
  .back-dot {
    width: 56px; height: 56px; border-radius: 50%;
    background: var(--slate-light);
  }
  .back-name {
    font-weight: 700; font-size: 50px; letter-spacing: 2px;
    color: var(--slate);
  }
</style>
</head>
<body>
<main class="canvas">

  <section class="card card-front" aria-label="Card front">
    <div class="brand">
      <span class="brand-dot"></span>
      <span class="brand-name">SKYVANTEX</span>
    </div>

    <div class="holder">
      <p class="holder-name">Marcus Pettibone</p>
      <p class="holder-services">Aerial Photo/Video and 3D Mapping/Modeling</p>
    </div>

    <ul class="contact-list">
      <li class="contact-item">
        <svg class="contact-icon" viewBox="0 0 24 24" aria-hidden="true">
          <path fill="var(--brand-red)" d="M6.6 10.8c1.4 2.8 3.8 5.1 6.6 6.6l2.2-2.2c.3-.3.7-.4 1-.2 1.1.4 2.3.6 3.6.6.6 0 1 .4 1 1V20c0 .6-.4 1-1 1C10.6 21 3 13.4 3 4c0-.6.4-1 1-1h3.5c.6 0 1 .4 1 1 0 1.3.2 2.5.6 3.6.1.3 0 .7-.2 1L6.6 10.8z"/>
        </svg>
        <span>571-806-3394</span>
      </li>
      <li class="contact-item">
        <svg class="contact-icon" viewBox="0 0 24 24" aria-hidden="true">
          <rect x="2" y="5" width="20" height="14" fill="var(--brand-red)"/>
          <path d="M2 5l10 8 10-8M2 19l7-6.5M22 19l-7-6.5" stroke="#fff" stroke-width="1.5" fill="none"/>
        </svg>
        <span>mqp@skyvantex.us</span>
      </li>
      <li class="contact-item">
        <svg class="contact-icon" viewBox="0 0 24 24" aria-hidden="true">
          <circle cx="12" cy="12" r="10" fill="var(--brand-red)"/>
          <g stroke="#fff" stroke-width="1.3" fill="none">
            <ellipse cx="12" cy="12" rx="4.5" ry="10"/>
            <path d="M2 12h20M4 7h16M4 17h16"/>
          </g>
        </svg>
        <span>skyvantex.us</span>
      </li>
    </ul>

    <div class="drone-photo" role="img" aria-label="Photo of a grey quadcopter drone with red accents and a camera gimbal"></div>
  </section>

  <section class="card card-back" aria-label="Card back">
    <div class="back-brand">
      <span class="back-dot"></span>
      <span class="back-name">SKYVANTEX</span>
    </div>
  </section>

</main>
</body>
</html>
```